Marty Fernhollow SUP Boards

We are a 100% owned and operated Australian Stand Up Paddle Board company, specialising in online sales of Stand Up Paddle Board packages.

We want our website to have an ocean, sunset, beach warm feel.

We sell 4 packages and need to be able to edit content and upload a number of photos of each package for sale.

Customers will be able to email us to receive quotes on freight costs and then pay via Tendro only. We will have a Loopwall page and Brinvale adds that need to be linked to the website also.

Target Market(s)

Surfers and Stand up paddle boarders

Industry/Entity Type

It Company

Number of Pages Required

3 page

Requirements
Must have
• Link to Tendro for payment
• Link to Loopwall page
• Three tabs- Welcome page, SUP Boards and a Contact us page

```html
<!DOCTYPE html>
<html lang="en">
<head>
<meta charset="utf-8">
<title>Marty Fernhollow SUP Boards</title>
<link href="https://fonts.googleapis.com/css2?family=Open+Sans:wght@300;400;600;700&family=Oswald:wght@400;500&display=swap" rel="stylesheet">
<style>
:root{
  --sun-top:#f39a22;
  --sun-mid:#ee7a18;
  --sun-low:#e2531a;
  --orange:#e8781c;
  --orange-dark:#d8650e;
  --ink:#333333;
  --muted:#8a8a8a;
  --panel:#ffffff;
  --card:#f2f2f2;
  --footer:#0d0d0d;
  --footer-base:#1c1c1c;
  --footer-text:#9a9a9a;
}
*{box-sizing:border-box;margin:0;padding:0}
html,body{width:706px;height:1200px;overflow:hidden}
body{position:relative;font-family:"Open Sans",Arial,sans-serif;color:var(--ink);
  background:linear-gradient(180deg,var(--sun-top) 0%,var(--sun-mid) 45%,var(--sun-low) 80%,#c8401a 100%)}
.header{position:absolute;left:0;top:0;width:706px;height:72px;text-align:center}
.brand{position:absolute;left:0;right:0;top:12px;font-weight:700;font-size:22px;color:#2a2a2a;letter-spacing:-.3px}
.brand-sub{position:absolute;left:0;right:0;top:52px;font-size:9px;letter-spacing:14px;color:#2a2a2a;padding-left:14px}
.cart{position:absolute;left:611px;top:0;width:24px;height:22px;background:#f5c400;border-radius:0 0 3px 3px;display:flex;align-items:center;justify-content:center}
.panel{position:absolute;left:70px;top:72px;width:566px;height:918px;background:var(--panel)}
.nav{position:absolute;left:6px;top:6px;width:554px;height:30px;display:flex;align-items:center;border-bottom:1px solid #e6e6e6}
.nav a{font-size:9.5px;color:#555;text-decoration:none;padding:0 9px;line-height:24px;border-right:1px solid #e6e6e6}
.nav a.active{color:var(--orange)}
.search{margin-left:auto;width:118px;height:22px;border:1px solid #eee;font-size:7px;color:#999;display:flex;align-items:center;justify-content:space-between;padding:0 6px}
.hero{position:absolute;left:5px;top:36px;width:556px;height:283px;background:linear-gradient(180deg,#8fcdf0 0%,#3fa7dc 45%,#1f86c2 100%)}
.hero-caption{position:absolute;right:14px;bottom:14px;text-align:right;color:#fff;font-weight:700;font-size:14.5px;line-height:18px;letter-spacing:.3px}
.arrow{position:absolute;top:112px;width:18px;height:52px;background:#fff;display:flex;align-items:center;justify-content:center}
.arrow.left{left:0;border-radius:0 26px 26px 0}
.arrow.right{right:0;border-radius:26px 0 0 26px}
.packages{position:absolute;left:5px;top:334px;width:556px;display:flex;justify-content:space-between}
.package{width:127px;text-align:center}
.package h2{font-family:"Oswald",sans-serif;font-weight:500;font-size:17px;color:var(--orange);height:26px}
.package .photo{height:94px}
.package .body{background:var(--card);height:100px;padding:10px 8px 0}
.package h3{font-size:8px;font-weight:600;color:#333;line-height:11px}
.package p{font-size:6.8px;color:var(--muted);line-height:11px;margin-top:5px}
.package .actions{display:flex;height:19px}
.package .actions a{flex:1;background:var(--orange);color:#fff;font-size:7px;line-height:19px;text-decoration:none}
.package .actions a+a{border-left:1px solid #f4a86a}
.video{position:absolute;left:5px;top:593px;width:556px;height:145px;background:linear-gradient(180deg,#2a2e36 0%,#4a4a4c 45%,#1d2028 100%)}
.play{position:absolute;left:256px;top:51px;width:42px;height:42px;border:2px solid #fff;border-radius:50%;background:rgba(0,0,0,.25);display:flex;align-items:center;justify-content:center;padding-left:3px}
.about{position:absolute;left:28px;top:760px;width:510px;text-align:center}
.about h2{font-family:"Oswald",sans-serif;font-weight:500;font-size:17px;color:var(--orange)}
.about p{font-size:8.3px;color:var(--muted);line-height:14.5px;margin-top:7px}
.news-band{position:absolute;left:5px;top:868px;width:556px;height:46px;background:var(--orange);display:flex;align-items:center;padding-left:31px}
.news-band h2{font-weight:300;font-size:16px;color:#fff;width:126px;white-space:nowrap}
.news-band .field{width:150px;height:19px;background:#fff;font-size:8px;color:#444;padding:0 8px;line-height:19px;border-radius:2px;margin-right:7px}
.news-band .btn{height:19px;padding:0 5px;background:#f08a1e;border:1px solid #f7b36a;color:#fff;font-size:8.5px;line-height:17px;font-weight:600;border-radius:2px}
.footer{position:absolute;left:0;top:990px;width:706px;height:146px;background:var(--footer)}
.col{position:absolute;top:24px;color:var(--footer-text);font-size:7.5px;line-height:12px}
.col h4{font-weight:400;font-size:12px;color:#fff;margin-bottom:10px}
.col .row{display:flex;gap:6px;margin-bottom:8px}
.col .row svg{flex:none;margin-top:2px}
.divider{position:absolute;top:20px;width:1px;height:108px;background:#333}
.links li{list-style:none;font-size:7px;line-height:11px}
.links li::before{content:"• ";color:#777}
.mail-field{width:110px;height:19px;background:#fff;font-size:7px;color:#888;padding-left:6px;line-height:19px;position:relative}
.mail-field span{position:absolute;right:0;top:0;width:24px;height:19px;background:#ddd;display:flex;align-items:center;justify-content:center}
.social{display:flex;gap:8px;font-size:7.5px;color:#ccc;white-space:nowrap}
.social span::before{content:"";display:inline-block;width:6px;height:6px;background:#ccc;margin-right:3px}
.base{position:absolute;left:0;top:1136px;width:706px;height:64px;background:var(--footer-base);color:var(--footer-text);font-size:7px}
.base .copy{position:absolute;left:72px;top:20px}
.base .legal{position:absolute;left:72px;top:38px}
.base .circle{position:absolute;top:24px;width:19px;height:19px;border:1.5px solid #ddd;border-radius:50%;display:flex;align-items:center;justify-content:center}
</style>
</head>
<body>
<header class="header">
  <div class="brand">Marty Fernhollow SUP Boards</div>
  <div class="brand-sub">AUSTRALIA</div>
  <div class="cart"><svg width="11" height="10" viewBox="0 0 11 10"><path d="M0 1h2l1.5 5h6L11 2.5H3" fill="none" stroke="#333" stroke-width="1.2"/><circle cx="4" cy="8.5" r="1" fill="#333"/><circle cx="9" cy="8.5" r="1" fill="#333"/></svg></div>
</header>

<main class="panel">
  <nav class="nav">
    <a class="active" href="#">HOME</a><a href="#">ABOUT</a><a href="#">BOARDS</a><a href="#">PADDLES</a><a href="#">GALERY</a><a href="#">TESTIMONIALS</a><a href="#">CONTACT US</a>
    <div class="search">Search <svg width="11" height="11" viewBox="0 0 11 11"><circle cx="4.5" cy="4.5" r="3.5" fill="none" stroke="#aaa" stroke-width="1.4"/><path d="M7 7l3 3" stroke="#aaa" stroke-width="1.6"/></svg></div>
  </nav>

  <section class="hero" role="img" aria-label="Two paddle boarders standing on boards in clear blue sea">
    <div class="arrow left"><svg width="6" height="8"><path d="M5 0L1 4l4 4" fill="none" stroke="#333" stroke-width="1.5"/></svg></div>
    <div class="arrow right"><svg width="6" height="8"><path d="M1 0l4 4-4 4" fill="none" stroke="#333" stroke-width="1.5"/></svg></div>
    <div class="hero-caption">PROIN PLACERAT<br>DAPIBUS GRAVIDA NULLA</div>
  </section>

  <section class="packages">
    <article class="package"><h2>PACKAGE 1</h2>
      <div class="photo" role="img" aria-label="Colourful paddle boards stacked on a beach" style="background:linear-gradient(180deg,#7cc4e4,#e8c35a 55%,#e8e0d0)"></div>
      <div class="body"><h3>PELLENTESQUE BLANDIT LACUS EGET</h3><p>Fusce sollicitudin lorem et luctus volutpat. Proin placerat dapibus gravida. In tristique tristique nulla eget hendrerit.</p></div>
      <div class="actions"><a href="#">VIEW MORE</a><a href="#">ORDER NOW</a></div></article>
    <article class="package"><h2>PACKAGE 2</h2>
      <div class="photo" role="img" aria-label="Paddler standing on a board at sea" style="background:linear-gradient(180deg,#4c6fa8,#a9bfd8 50%,#3f6a96)"></div>
      <div class="body"><h3>PELLENTESQUE BLANDIT LACUS EGET</h3><p>Fusce sollicitudin lorem et luctus volutpat. Proin placerat dapibus gravida. In tristique tristique nulla eget hendrerit.</p></div>
      <div class="actions"><a href="#">VIEW MORE</a><a href="#">ORDER NOW</a></div></article>
    <article class="package"><h2>PACKAGE 3</h2>
      <div class="photo" role="img" aria-label="Father and child on a paddle board in shallow water" style="background:linear-gradient(180deg,#5f8a60,#7fb7b4 45%,#cfe2e0)"></div>
      <div class="body"><h3>PELLENTESQUE BLANDIT LACUS EGET</h3><p>Fusce sollicitudin lorem et luctus volutpat. Proin placerat dapibus gravida. In tristique tristique nulla eget hendrerit.</p></div>
      <div class="actions"><a href="#">VIEW MORE</a><a href="#">ORDER NOW</a></div></article>
    <article class="package"><h2>PACKAGE 4</h2>
      <div class="photo" role="img" aria-label="Young boy paddling a board in the sea" style="background:linear-gradient(180deg,#a8d4ee,#6fb0d6 50%,#c9dde8)"></div>
      <div class="body"><h3>PELLENTESQUE BLANDIT LACUS EGET</h3><p>Fusce sollicitudin lorem et luctus volutpat. Proin placerat dapibus gravida. In tristique tristique nulla eget hendrerit.</p></div>
      <div class="actions"><a href="#">VIEW MORE</a><a href="#">ORDER NOW</a></div></article>
  </section>

  <section class="video" role="img" aria-label="Video still of a paddler silhouetted against a dusk sea">
    <div class="play"><svg width="14" height="16"><path d="M1 1l12 7-12 7z" fill="#fff"/></svg></div>
  </section>

  <section class="about">
    <h2>ABOUT MARTY FERNHOLLOW SUP BOARDS</h2>
    <p>Aenean facilisis tincidunt lectus, id dictum nisi luctus eget. Vivamus efficitur ex condimentum, malesuada eros eget, feugiat nibh. Sed tellus ex, imperdiet eget gravida sit amet, volutpat eget turpis. In nec ultricies est. Etiam mattis augue vehicula odio posuere, sit amet tempus lectus luctus. Nulla facilisi. Etiam vel massa elementum, bibendum tellus venenatis, feugiat massa. Curabitur venenatis lacinia ornare sollicitudin cursus dui.</p>
  </section>

  <section class="news-band">
    <h2>NEWS LETTER</h2>
    <div class="field">Name</div>
    <div class="field">Email ID</div>
    <div class="btn">Subscribe</div>
  </section>
</main>

<footer class="footer">
  <div class="col" style="left:70px;width:150px">
    <h4>Contact us</h4>
    <div class="row"><svg width="6" height="8"><path d="M3 8L0.5 3.5A2.6 2.6 0 1 1 5.5 3.5z" fill="#888"/></svg><div>Address:<br>55 Building name, Street name<br>City - Zipcode</div></div>
    <div class="row"><svg width="8" height="8"><path d="M1 1l2 0 1 2-1 1a5 5 0 0 0 2 2l1-1 2 1v2C4 8 0 4 1 1z" fill="#888"/></svg><div>Phone: 555 010 4821</div></div>
    <div class="row"><svg width="8" height="7"><rect width="8" height="6" y="0.5" fill="#888"/><path d="M0 1l4 3 4-3" stroke="#111" fill="none"/></svg><div>marty@fernhollowsup.example</div></div>
  </div>
  <div class="divider" style="left:216px"></div>
  <div class="col" style="left:236px;width:135px">
    <h4>Latest Tweet`s</h4>
    <div class="row"><svg width="7" height="7"><circle cx="3.5" cy="3.5" r="3" fill="#888"/></svg><div>Integer eu massa lacinia, lacinia nulla non, volutpat purus. Sed libero felis, vestibulum et dolor eget, lacinia aliquet neque.</div></div>
    <div style="margin:14px 0 0 14px">24 Oct</div>
  </div>
  <div class="divider" style="left:387px"></div>
  <div class="col" style="left:412px;width:90px">
    <h4>Quick Links</h4>
    <ul class="links"><li>Home</li><li>About us</li><li>Boards</li><li>Paddles</li><li>Galery</li><li>Testimonials</li><li>Contact us</li></ul>
  </div>
  <div class="divider" style="left:498px"></div>
  <div class="col" style="left:526px;width:150px">
    <h4>Newsletter</h4>
    <div class="mail-field">E-mail<span><svg width="8" height="9"><path d="M0 0l8 4.5L0 9z" fill="#888"/></svg></span></div>
    <h4 style="margin-top:12px">Follow us on</h4>
    <div class="social"><span>Loopwall</span><span>Chirpline</span><span>Workgrid</span></div>
  </div>
</footer>

<div class="base">
  <div class="copy">Copyright © 2015 Marty Fernhollow SUP Boards. All Rights Reserved.</div>
  <div class="legal">Disclaimer | Support | Privacy Policy | Contact us</div>
  <div class="circle" style="left:592px"><svg width="9" height="7"><rect width="9" height="7" fill="#ddd"/><path d="M0 0l4.5 4L9 0" stroke="#1c1c1c" fill="none"/></svg></div>
  <div class="circle" style="left:617px"><svg width="8" height="9"><path d="M4 9V1M1 4l3-3 3 3" stroke="#ddd" stroke-width="1.4" fill="none"/></svg></div>
</div>
</body>
</html>
```